Lantern of Renewal needs a business card design

I need a business card design for my company to promote my new Christian non-fiction book, "Where The River Bends Home." I also want it to promote my web site, www.lanternofrenewalbks.com. The book is about empowering people to be transformed through a deeper relationship with God. I am picturing a design with a dove over water that matches the colors of my book cover, blue, white, yellow, and orange. Fire and light would also be possible elements of the design. I would like to be able to use the dove by itself as a logo for my business. This is my first book and I do not know if others will follow. The name of my publishing company is Silver Harvest Press, named after Gideon in the Bible story from the book of Judges. My book was independently published and was recently selected as a finalist for the 2015 Bright Horizon SMALLPRESS book award in the Christian non-fiction genre.

Target Market(s)

People who are hungry for more of God and who want to experience deep change in their lives.

Industry/Entity Type

Business

Contact Information for Business Card

Dana Whitcombe
Author
Where The River Bends Home
4287 Maple Orchard Lane
Austin, Texas 78651-2097
512-555-0143 512-555-0178
dana-whitcombe@examplemail.net
www.lanternofrenewalbks.com

Colors
0355a3
3377b5
85acd3
cedeed
fbee3e
ffc214

Requirements
Must have
• A dove with a blue background, peaceful and appealing
Nice to have
• Water and fire or light
Should not have
• Violence or fear-producing images

```html
<!DOCTYPE html>
<html lang="en">
<head>
<meta charset="utf-8">
<title>Dana Whitcombe — Business Card</title>
<link rel="stylesheet" href="https://fonts.googleapis.com/css2?family=Arimo:wght@400;700&family=Libre+Baskerville&family=Playball&display=swap">
<style>
  :root {
    --page-bg: #e4e4e2;
    --navy-deep: #15226b;
    --navy-mid: #243c9c;
    --blue-bright: #3377b5;
    --blue-soft: #85acd3;
    --ice: #cedeed;
    --card-blue: #0a53a3;
    --gold: #ffc214;
    --gold-line: #f2b51a;
    --url-blue: #0b3c9a;
    --white: #ffffff;
  }
  * { box-sizing: border-box; margin: 0; padding: 0; }
  html, body { width: 1200px; height: 1200px; overflow: hidden; }
  body {
    background: var(--page-bg);
    font-family: "Arimo", Arial, sans-serif;
    position: relative;
  }
  .card {
    position: absolute;
    left: 160px;
    width: 880px;
    height: 503px;
    overflow: hidden;
    box-shadow: 0 6px 18px rgba(0,0,0,0.18);
  }
  /* Front side */
  .card-front { top: 70px; }
  .front-water {
    position: absolute; inset: 0;
    background:
      radial-gradient(circle at 22% 30%, rgba(133,172,211,0.35), transparent 35%),
      radial-gradient(circle at 70% 20%, rgba(51,119,181,0.45), transparent 40%),
      radial-gradient(circle at 85% 80%, rgba(51,119,181,0.35), transparent 40%),
      radial-gradient(circle at 35% 85%, rgba(36,60,156,0.6), transparent 45%),
      linear-gradient(135deg, var(--navy-deep), var(--navy-mid) 55%, #1c2f86);
  }
  .front-brand {
    position: absolute; top: 72px; left: 0; right: 0;
    display: flex; justify-content: center; align-items: center; gap: 12px;
    padding-left: 120px;
    color: var(--ice);
    font-size: 24px; font-weight: 700;
  }
  .brand-dot {
    width: 22px; height: 22px; border-radius: 50%;
    background: var(--blue-soft);
  }
  .author-name {
    position: absolute; top: 150px; left: 0; right: 0;
    text-align: center; padding-left: 60px;
    color: var(--white);
    font-size: 66px; font-weight: 700; letter-spacing: 0.5px;
  }
  .author-role {
    position: absolute; top: 232px; left: 0; right: 0;
    text-align: center; padding-left: 20px;
    color: var(--ice);
    font-size: 26px;
  }
  .url-band {
    position: absolute; top: 282px; left: 0; right: 0;
    height: 56px;
    background: var(--gold);
    display: flex; align-items: center;
    padding-left: 48px;
  }
  .url-band span {
    color: var(--url-blue);
    font-size: 36px;
  }
  /* Back side */
  .card-back { top: 627px; background: var(--card-blue); }
  .book-title {
    position: absolute; top: 62px; left: 250px; width: 600px;
    text-align: center; color: var(--white);
  }
  .book-title .title-main {
    font-family: "Libre Baskerville", Georgia, serif;
    font-size: 34px; letter-spacing: 0.5px; display: block;
  }
  .book-title .title-script {
    font-family: "Playball", cursive;
    font-size: 40px; display: block; margin-top: 2px;
  }
  .title-rule {
    position: absolute; top: 192px; left: 262px; width: 576px;
    height: 3px; background: var(--gold-line);
  }
  .back-brand {
    position: absolute; top: 250px; left: 40px; width: 190px;
    display: flex; align-items: center; gap: 10px;
    color: var(--ice); font-size: 21px; font-weight: 700; line-height: 1.2;
  }
  .back-brand .brand-dot { flex: none; }
  .contact-list {
    position: absolute; top: 226px; left: 262px;
    list-style: none;
  }
  .contact-list li {
    display: flex; align-items: center; gap: 16px;
    color: var(--ice); font-size: 24px;
    height: 52px;
  }
  .contact-list svg { width: 24px; height: 24px; flex: none; }
</style>
</head>
<body>
  <section class="card card-front">
    <div class="front-water" role="img" aria-label="Deep blue watercolour water texture with light reflections"></div>
    <div class="front-brand"><span class="brand-dot"></span>Lantern of Renewal</div>
    <h1 class="author-name">Dana Whitcombe</h1>
    <p class="author-role">(Author)</p>
    <div class="url-band"><span>www.lanternofrenewalbks.com</span></div>
  </section>

  <section class="card card-back">
    <h2 class="book-title">
      <span class="title-main">WHERE THE RIVER BENDS</span>
      <span class="title-script">Home</span>
    </h2>
    <div class="title-rule"></div>
    <div class="back-brand"><span class="brand-dot"></span>Lantern of Renewal</div>
    <ul class="contact-list">
      <li>
        <svg viewBox="0 0 24 24" fill="none" stroke="#cedeed" stroke-width="1.8"><rect x="7" y="2" width="10" height="20" rx="2"/><line x1="11" y1="18.5" x2="13" y2="18.5"/></svg>
        512-555-0143, 512-555-0178
      </li>
      <li>
        <svg viewBox="0 0 24 24" fill="#cedeed"><path d="M2 5h20v14H2z"/><path d="M2 5l10 8 10-8" fill="none" stroke="#0a53a3" stroke-width="1.8"/></svg>
        dana-whitcombe@examplemail.net
      </li>
      <li>
        <svg viewBox="0 0 24 24" fill="#cedeed"><path d="M12 2a7 7 0 0 0-7 7c0 5 7 13 7 13s7-8 7-13a7 7 0 0 0-7-7z"/><circle cx="12" cy="9" r="2.6" fill="#0a53a3"/></svg>
        4287 Maple Orchard Lane Austin, Texas
      </li>
    </ul>
  </section>
</body>
</html>
```